Biz cards and stationary design
for Harbor Pathways
Project: Biz cards and stationary design
Biz cards and stationary design  - Consulting
Creative Brief
Professional
Tessa R Windrow
President
27816 Dovelin Court Haymarket, VA 20174
tessa.windrow@harborpathways-example.com
http://www.harborpathways-example.com

```html
<!DOCTYPE html>
<html lang="en">
<head>
<meta charset="utf-8">
<title>Harbor Pathways — Business Cards and Stationery</title>
<link rel="stylesheet" href="https://fonts.googleapis.com/css2?family=Cinzel:wght@700&family=Open+Sans:wght@400;600&display=swap">
<style>
  :root {
    --board: #ece4d8;
    --board-right: #e4d7c4;
    --paper: #ffffff;
    --crimson: #a3161c;
    --crimson-deep: #7c0d12;
    --gold: #f2b01e;
    --gold-light: #ffd45a;
    --ink: #5a5a5a;
    --caption: #6b5a48;
    --flap-line: #d9d9d9;
  }
  * { box-sizing: border-box; margin: 0; padding: 0; }
  html, body { width: 1200px; height: 446px; overflow: hidden; }
  body {
    position: relative;
    background: var(--board);
    font-family: "Open Sans", Arial, sans-serif;
    color: var(--ink);
  }
  .board-right {
    position: absolute; left: 773px; top: 0; width: 427px; height: 446px;
    background: var(--board-right);
  }
  .piece {
    position: absolute;
    background: var(--paper);
    box-shadow: 0 1px 4px rgba(0,0,0,.25);
    overflow: hidden;
  }
  .piece svg.wave { position: absolute; left: 0; bottom: 0; width: 100%; }
  .brand {
    position: absolute;
    font-family: "Cinzel", Georgia, serif;
    font-weight: 700;
    color: var(--crimson);
    white-space: nowrap;
    letter-spacing: .4px;
  }
  .caption {
    position: absolute;
    font-size: 5px;
    letter-spacing: .6px;
    text-transform: uppercase;
    color: var(--caption);
    white-space: nowrap;
  }

  /* business cards */
  .card { left: 12px; width: 67px; height: 38px; }
  .card--front { top: 149px; }
  .card--back { top: 240px; }
  .card .brand { font-size: 5px; left: 0; right: 0; text-align: center; top: 8px; }
  .card .detail {
    position: absolute; left: 4px; right: 4px; top: 17px;
    font-size: 2.4px; line-height: 1.35; text-align: center;
  }

  /* letterheads */
  .letterhead { top: 7px; width: 288px; height: 401px; }
  .letterhead--one { left: 163px; }
  .letterhead--two { left: 475px; }
  .letterhead--one .brand { font-size: 8px; left: 40px; top: 24px; }
  .letterhead--two .brand { font-size: 8px; left: 0; right: 0; text-align: center; top: 24px; }
  .contact-block {
    position: absolute; left: 196px; top: 20px; width: 84px;
    font-size: 2.6px; line-height: 1.5; color: var(--ink); white-space: nowrap;
  }
  .footer-block {
    position: absolute; right: 20px; bottom: 14px;
    font-size: 2.6px; line-height: 1.5; color: var(--paper); text-align: right;
  }

  /* envelopes */
  .envelope-stack { position: absolute; left: 826px; top: 10px; width: 364px; height: 236px; }
  .envelope-front { left: 800px; top: 257px; width: 392px; height: 140px; }
  .envelope-front .return {
    position: absolute; left: 28px; top: 50px; font-size: 2.6px; line-height: 1.5;
  }
  .envelope-front .recipient {
    position: absolute; left: 190px; top: 70px; font-size: 3.2px; line-height: 1.5;
  }
  .envelope-stack .brand-svg {
    font-family: "Cinzel", Georgia, serif; font-weight: 700; fill: var(--crimson); font-size: 7px;
  }
</style>
</head>
<body>
<svg width="0" height="0" style="position:absolute">
  <defs>
    <linearGradient id="crimsonFill" x1="0" y1="0" x2="1" y2="1">
      <stop offset="0" stop-color="#c0242a"/>
      <stop offset="1" stop-color="#7c0d12"/>
    </linearGradient>
    <linearGradient id="goldFill" x1="0" y1="0" x2="1" y2="0">
      <stop offset="0" stop-color="#ffd45a"/>
      <stop offset="1" stop-color="#f2a51a"/>
    </linearGradient>
    <symbol id="pageWave" viewBox="0 0 216 70" preserveAspectRatio="none">
      <path d="M0 30 C50 8 120 44 216 0 L216 8 C130 50 60 20 0 40 Z" fill="url(#goldFill)"/>
      <path d="M0 40 C60 20 130 52 216 10 L216 70 L0 70 Z" fill="url(#crimsonFill)"/>
    </symbol>
  </defs>
</svg>

<div class="board-right"></div>

<p class="caption" style="left:12px;top:125px">Stationery Concepts</p>

<section class="piece card card--front">
  <p class="brand">Harbor Pathways</p>
  <p class="detail"><strong>Tessa R Windrow</strong> · President</p>
  <svg class="wave" height="11"><use href="#pageWave"/></svg>
</section>
<p class="caption" style="left:12px;top:192px">Business Card Front</p>

<section class="piece card card--back">
  <p class="brand" style="top:15px">Harbor Pathways</p>
  <svg class="wave" height="8"><use href="#pageWave"/></svg>
</section>
<p class="caption" style="left:12px;top:283px">Business Card Back</p>

<section class="piece letterhead letterhead--one">
  <p class="brand">Harbor Pathways</p>
  <div class="contact-block">
    Tessa R Windrow, President<br>
    27816 Dovelin Court<br>
    Haymarket, VA 20174<br>
    tessa.windrow@harborpathways-example.com<br>
    http://www.harborpathways-example.com
  </div>
  <svg class="wave" height="76"><use href="#pageWave"/></svg>
</section>
<p class="caption" style="left:270px;top:422px">Letter Head Option 1</p>

<section class="piece letterhead letterhead--two">
  <p class="brand">Harbor Pathways</p>
  <svg class="wave" height="76"><use href="#pageWave"/></svg>
  <div class="footer-block">
    27816 Dovelin Court Haymarket, VA 20174<br>
    tessa.windrow@harborpathways-example.com<br>
    http://www.harborpathways-example.com
  </div>
</section>
<p class="caption" style="left:582px;top:422px">Letter Head Option 2</p>

<svg class="envelope-stack" viewBox="0 0 364 236">
  <!-- back envelope, crimson -->
  <rect x="0" y="0" width="364" height="82" rx="8" fill="url(#crimsonFill)"/>
  <!-- middle envelope, gold flap -->
  <rect x="0" y="84" width="364" height="90" fill="#ffffff"/>
  <path d="M0 84 H364 V100 C300 150 64 150 0 100 Z" fill="url(#goldFill)"/>
  <!-- front envelope, white open flap -->
  <rect x="0" y="150" width="364" height="86" fill="#ffffff" stroke="var(--flap-line)" stroke-width=".6"/>
  <path d="M0 150 H364 V160 C300 200 64 200 0 160 Z" fill="#f7f7f7" stroke="var(--flap-line)" stroke-width=".6"/>
  <text class="brand-svg" x="182" y="214" text-anchor="middle">Harbor Pathways</text>
</svg>

<section class="piece envelope-front">
  <div class="return">
    Tessa R Windrow<br>
    27816 Dovelin Court<br>
    Haymarket, VA 20174
  </div>
  <div class="recipient">
    Recipient Name<br>
    Street Address<br>
    City, State Zip
  </div>
  <svg class="wave" height="34" viewBox="0 0 392 34" preserveAspectRatio="none">
    <path d="M0 20 C110 4 240 28 392 2 L392 8 C240 34 110 12 0 26 Z" fill="url(#goldFill)"/>
    <path d="M0 26 C110 12 240 36 392 8 L392 34 L0 34 Z" fill="url(#crimsonFill)"/>
  </svg>
</section>
<p class="caption" style="left:950px;top:422px">Envelope Option 1</p>
</body>
</html>
```